Logistics Business Needs a Business Card Design

We need a business card design for our logistics company. Previously we have engaged a designer to do a design as enclosed but it is not up to our expectation. We would like to see some changes, such as a fading blue line at the top of the business card (front) and a partial globe outline at the bottom right corner of the business card (front). Also enclosed are the particulars of the staff's business card required (note that our office phone number has changed to +65 6283 5170 & fax number is not required). Please produce the design file in cdr format. Thanks.

```html
<!DOCTYPE html>
<html lang="en">
<head>
<meta charset="utf-8">
<title>Orbis Link – Business Card</title>
<link rel="stylesheet" href="https://fonts.googleapis.com/css2?family=Tinos:wght@400;700&family=Noto+Serif+SC:wght@500&display=swap">
<style>
  :root {
    --brand-blue: #1d4a8e;
    --band-navy: #123f75;
    --ink: #1f1f1f;
    --paper: #ffffff;
    --frame: #8a8a8a;
    --globe-light: #bfe6f5;
    --globe-mid: #4aa3d6;
    --globe-deep: #1a5d9c;
    --corner-light: #e6eefa;
    --corner-mid: #9cb8e6;
    --corner-deep: #3a6cc0;
  }
  * { margin: 0; padding: 0; box-sizing: border-box; }
  html, body { width: 1200px; height: 690px; overflow: hidden; background: var(--paper); }
  .card {
    position: relative;
    width: 1200px;
    height: 690px;
    background: var(--paper);
    border: 2px solid var(--frame);
    overflow: hidden;
    font-family: "Tinos", "Times New Roman", serif;
  }
  .top-band {
    position: absolute; left: 0; top: 0; width: 100%; height: 16px;
    background: linear-gradient(90deg, var(--band-navy), #1f5a9c 60%, var(--band-navy));
  }
  .hero-globe {
    position: absolute; left: 30px; top: 99px; width: 302px; height: 302px;
    border-radius: 50%;
    background: radial-gradient(circle at 38% 32%, var(--globe-light) 0%, var(--globe-mid) 45%, var(--globe-deep) 100%);
  }
  .company-name {
    position: absolute; left: 366px; top: 100px;
    font-size: 62px; font-weight: 400; color: var(--brand-blue); letter-spacing: 0.5px; white-space: nowrap;
  }
  .company-reg {
    position: absolute; left: 366px; top: 188px;
    font-size: 47px; color: var(--ink); white-space: nowrap;
  }
  .person-name {
    position: absolute; left: 366px; top: 296px;
    font-size: 47px; font-weight: 700; color: var(--brand-blue); white-space: nowrap;
  }
  .person-name-cn {
    position: absolute; left: 664px; top: 296px;
    font-family: "Noto Serif SC", serif; font-size: 38px; font-weight: 500;
    color: var(--brand-blue); letter-spacing: 13px; white-space: nowrap;
  }
  .person-title, .person-mobile {
    position: absolute; left: 366px;
    font-size: 33px; font-weight: 700; color: var(--brand-blue); white-space: nowrap;
  }
  .person-title { top: 359px; }
  .person-mobile { top: 409px; }
  .office-address, .office-tel, .office-email {
    position: absolute; font-size: 40px; color: var(--brand-blue); white-space: nowrap;
  }
  .office-address { left: 43px; top: 529px; }
  .office-tel { left: 46px; top: 587px; font-size: 39px; }
  .office-email { left: 407px; top: 583px; }
  .corner-globe {
    position: absolute; left: 1034px; top: 480px; width: 210px; height: 210px;
    border-radius: 50%;
    background: radial-gradient(circle at 35% 30%, var(--corner-light) 0%, var(--corner-mid) 55%, var(--corner-deep) 100%);
  }
</style>
</head>
<body>
  <div class="card">
    <div class="top-band"></div>

    <div class="hero-globe" role="img" aria-label="Glossy blue globe with world map and glowing network connection lines"></div>

    <div class="company-name">ORBIS LINK PVT. LTD.</div>
    <div class="company-reg">Co. Reg. No: 201538274K</div>

    <div class="person-name">Marcus Tan</div>
    <div class="person-name-cn">陈志豪</div>
    <div class="person-title">Executive Director</div>
    <div class="person-mobile">Hp: +65 9153 6047</div>

    <div class="office-address">21 Kallang Way Harbour Point #05-08 Singapore 349245</div>
    <div class="office-tel">Tel: +65 6283 5170</div>
    <div class="office-email">Email: marcus.tan@orbislink.com</div>

    <div class="corner-globe" role="img" aria-label="Partial blue wireframe globe outline in the corner"></div>
  </div>
</body>
</html>
```